Out of town New Masters of Accounting

size of ad is 7” x 9.6”
please leave one inch on bottom for footer
We want to attract out of town students to join this master's in accounting program.
You DO NOT  have to use a picture of a person.
But if you do, it should be a  male with a white shirt and should not have long hair.(look like a young executive)
THE TEXT OF THE AD IS IN THE ATTACHMENTS
THE CAP LETTERS ARE THE INSTRUCTIONS

The age we are trying to attract is from 20-30 of ages.
- a clear ad .. the text should not take up the entire ad.. it should not be very crowded -
it should be an attractive ad that people would want to see and stand out
- the text very big and take up the entire ad

```html
<!DOCTYPE html>
<html lang="en">
<head>
<meta charset="utf-8">
<title>Masters of Science in Accounting – Remote Program</title>
<link href="https://fonts.googleapis.com/css2?family=Montserrat:wght@400;500;600;700;800;900&display=swap" rel="stylesheet">
<style>
  :root {
    --blue: #228ed9;
    --blue-line: #4aa6e6;
    --ink: #111111;
    --heading: #2e2e2e;
    --paper: #f6f7f9;
    --white: #ffffff;
    --star: #ffe11a;
    --kraft: #d9a877;
    --badge-orange: #f0a020;
    --footer-dark: #000000;
  }
  * { margin: 0; padding: 0; box-sizing: border-box; }
  html, body { width: 846px; height: 1200px; overflow: hidden; }
  body { font-family: 'Montserrat', sans-serif; background: var(--white); }
  .ad { position: relative; width: 846px; height: 1200px; overflow: hidden; background: var(--white); }

  .hero { position: absolute; left: 0; top: 0; width: 846px; height: 620px; background: var(--paper); }
  .hero-photo {
    position: absolute; left: 455px; top: 0; width: 391px; height: 620px;
    background: linear-gradient(135deg, rgba(246,247,249,0) 0%, rgba(246,247,249,0) 38%, #c9b79c 50%, var(--kraft) 62%, #d6a574 100%);
  }
  .ranking-badge { position: absolute; left: 52px; top: 22px; width: 110px; height: 110px; border-radius: 50%; background: var(--badge-orange); }

  .headline { position: absolute; left: 46px; top: 228px; font-size: 74px; font-weight: 800; color: var(--heading); letter-spacing: -1px; line-height: 1; }
  .subhead { position: absolute; left: 48px; top: 314px; font-size: 32px; font-weight: 500; color: var(--heading); line-height: 34px; letter-spacing: 0.5px; }
  .rule { position: absolute; left: 48px; top: 399px; width: 144px; height: 3px; background: var(--heading); }

  .date-box { position: absolute; left: 48px; top: 443px; width: 237px; height: 103px; background: var(--blue); }
  .date-box .date { position: absolute; left: 14px; top: 12px; font-size: 33px; font-weight: 900; color: var(--ink); letter-spacing: 0.5px; }
  .date-box .divider { position: absolute; left: 0; top: 57px; width: 237px; height: 1px; background: var(--blue-line); }
  .date-box .offer { position: absolute; left: 11px; top: 66px; font-size: 19px; font-weight: 800; color: var(--white); text-decoration: underline; text-underline-offset: 3px; }

  .band { position: absolute; left: 0; top: 620px; width: 846px; height: 238px; background: var(--blue); }
  .band .split { position: absolute; left: 425px; top: 0; width: 1px; height: 238px; background: var(--blue-line); }
  .career { position: absolute; left: 77px; top: 43px; font-size: 33px; font-weight: 800; color: var(--ink); line-height: 31px; }
  .program { position: absolute; left: 77px; top: 124px; font-size: 24px; font-weight: 600; color: var(--white); line-height: 29px; }
  .program .degree { text-decoration: underline; text-underline-offset: 3px; }
  .program .field { font-weight: 500; }

  .rating { position: absolute; left: 475px; top: 49px; width: 340px; }
  .rating .ranker { font-size: 26px; font-weight: 700; color: var(--ink); }
  .rating .stars { margin-top: 4px; height: 22px; }
  .rating .note { margin-top: 6px; font-size: 16px; font-weight: 500; color: var(--white); line-height: 19.5px; }
  .rating .note strong { font-weight: 800; }

  .duration-badge { position: absolute; left: 571px; top: 835px; width: 184px; height: 184px; border-radius: 50%; background: var(--white); box-shadow: 0 4px 14px rgba(0,0,0,0.12); }
  .duration-badge svg { position: absolute; left: 0; top: 0; }

  .placement { position: absolute; left: 77px; top: 902px; font-size: 25px; font-weight: 700; color: var(--ink); line-height: 30px; }
  .benefits { position: absolute; left: 92px; top: 980px; list-style: none; font-size: 21px; font-weight: 400; color: var(--ink); line-height: 26px; }
  .benefits li { position: relative; padding-left: 15px; }
  .benefits li::before { content: ""; position: absolute; left: 0; top: 10px; width: 8px; height: 8px; border-radius: 50%; background: var(--blue); }

  .footer { position: absolute; left: 0; top: 1117px; width: 846px; height: 83px; }
  .footer .call { position: absolute; left: 0; top: 0; width: 426px; height: 83px; background: var(--footer-dark); }
  .footer .contact { position: absolute; left: 426px; top: 0; width: 420px; height: 83px; background: var(--blue); }
  .call .label { position: absolute; left: 104px; top: 17px; font-size: 14px; font-weight: 500; color: var(--blue); }
  .call .phone { position: absolute; left: 102px; top: 29px; font-size: 33px; font-weight: 500; color: var(--white); letter-spacing: 1px; }
  .call svg { position: absolute; left: 77px; top: 42px; }
  .contact .item { position: absolute; font-size: 12px; font-weight: 500; color: var(--white); line-height: 15px; }
  .contact .address { left: 57px; top: 36px; }
  .contact .online { left: 234px; top: 36px; }
  .contact svg { position: absolute; }
</style>
</head>
<body>
<div class="ad">
  <section class="hero">
    <div class="hero-photo" role="img" aria-label="Photo of a gel pen lying beside a kraft-paper spiral notebook"></div>
    <div class="ranking-badge" role="img" aria-label="Ranking badge"></div>
    <h1 class="headline">All New!</h1>
    <p class="subhead">Remote program for<br>out of town students</p>
    <div class="rule"></div>
    <div class="date-box">
      <div class="date">AUGUST 17</div>
      <div class="divider"></div>
      <div class="offer">NEW LOWER PRICES</div>
    </div>
  </section>

  <section class="band">
    <div class="split"></div>
    <h2 class="career">Advance further<br>in your career</h2>
    <p class="program"><span class="degree">Masters of Science</span><br><span class="field">in Accounting</span></p>
    <div class="rating">
      <div class="ranker">Gradlane</div>
      <svg class="stars" width="120" height="22" viewBox="0 0 120 22" aria-label="Five stars">
        <g fill="var(--star)">
          <polygon points="10,1 12.4,7.8 19.5,7.8 13.8,12 16,19 10,14.8 4,19 6.2,12 0.5,7.8 7.6,7.8"/>
          <polygon transform="translate(25 0)" points="10,1 12.4,7.8 19.5,7.8 13.8,12 16,19 10,14.8 4,19 6.2,12 0.5,7.8 7.6,7.8"/>
          <polygon transform="translate(49 0)" points="10,1 12.4,7.8 19.5,7.8 13.8,12 16,19 10,14.8 4,19 6.2,12 0.5,7.8 7.6,7.8"/>
          <polygon transform="translate(73 0)" points="10,1 12.4,7.8 19.5,7.8 13.8,12 16,19 10,14.8 4,19 6.2,12 0.5,7.8 7.6,7.8"/>
          <polygon transform="translate(96 0)" points="10,1 12.4,7.8 19.5,7.8 13.8,12 16,19 10,14.8 4,19 6.2,12 0.5,7.8 7.6,7.8"/>
        </g>
      </svg>
      <p class="note"><strong>Harlow Bridge University (HBU)</strong><br>Master in Accounting Program received<br>the <strong>highest possible star rating.</strong></p>
    </div>
  </section>

  <div class="duration-badge">
    <svg width="184" height="184" viewBox="0 0 184 184">
      <defs><clipPath id="inner"><circle cx="92" cy="92" r="83"/></clipPath></defs>
      <circle cx="92" cy="92" r="83" fill="var(--blue)"/>
      <g clip-path="url(#inner)">
        <path d="M17 92 A75 75 0 0 1 167 92 Z" fill="var(--white)"/>
      </g>
      <g fill="var(--blue)">
        <polygon transform="translate(81 28) scale(1.1)" points="10,1 12.4,7.8 19.5,7.8 13.8,12 16,19 10,14.8 4,19 6.2,12 0.5,7.8 7.6,7.8"/>
        <polygon transform="translate(55 40) scale(0.7)" points="10,1 12.4,7.8 19.5,7.8 13.8,12 16,19 10,14.8 4,19 6.2,12 0.5,7.8 7.6,7.8"/>
        <polygon transform="translate(115 40) scale(0.7)" points="10,1 12.4,7.8 19.5,7.8 13.8,12 16,19 10,14.8 4,19 6.2,12 0.5,7.8 7.6,7.8"/>
      </g>
      <text x="92" y="78" text-anchor="middle" font-family="Montserrat, sans-serif" font-size="14" font-weight="800" fill="var(--ink)">SUNCREST</text>
      <text x="92" y="109" text-anchor="middle" font-family="Montserrat, sans-serif" font-size="11" font-weight="600" fill="var(--ink)">A masters in only</text>
      <text x="92" y="127" text-anchor="middle" font-family="Montserrat, sans-serif" font-size="17" font-weight="800" fill="var(--white)">15 months</text>
      <g fill="none" stroke="var(--white)" stroke-width="1.3" stroke-linecap="round">
        <rect x="84" y="140" width="7" height="18" rx="3" transform="rotate(45 87 149)"/>
        <line x1="90" y1="146" x2="99" y2="137"/>
        <line x1="94" y1="150" x2="103" y2="141"/>
      </g>
    </svg>
  </div>

  <h3 class="placement">Keystone Career Network<br>Job Placement Advantage</h3>
  <ul class="benefits">
    <li>96% placement rate</li>
    <li>8 placement coordinators</li>
    <li>Decades of relationships with 100’s of firm</li>
  </ul>

  <footer class="footer">
    <div class="call">
      <div class="label">Give us a call</div>
      <svg width="14" height="22" viewBox="0 0 14 22"><rect x="1" y="1" width="12" height="20" rx="2" fill="none" stroke="var(--white)" stroke-width="2"/><rect x="3" y="4" width="8" height="11" fill="var(--white)"/><circle cx="7" cy="18" r="1.2" fill="var(--white)"/></svg>
      <div class="phone">900 555 0142</div>
    </div>
    <div class="contact">
      <svg style="left:41px;top:37px" width="10" height="14" viewBox="0 0 10 14"><path d="M5 0.5 A4.5 4.5 0 0 1 9.5 5 C9.5 8 5 13.5 5 13.5 C5 13.5 0.5 8 0.5 5 A4.5 4.5 0 0 1 5 0.5 Z" fill="var(--white)"/><circle cx="5" cy="5" r="1.7" fill="var(--blue)"/></svg>
      <div class="item address">48 Maple Crest Rd.<br>Lindon, FL 200410</div>
      <svg style="left:215px;top:38px" width="12" height="12" viewBox="0 0 12 12"><circle cx="6" cy="6" r="2.2" fill="none" stroke="var(--white)" stroke-width="1.4"/><path d="M8.2 4 V7 C8.2 8.5 10.8 8.5 10.8 6 A4.8 4.8 0 1 0 8.5 10.2" fill="none" stroke="var(--white)" stroke-width="1.4"/></svg>
      <svg style="left:215px;top:53px" width="12" height="12" viewBox="0 0 12 12"><circle cx="6" cy="6" r="5.5" fill="var(--white)"/><path d="M3 3 Q5 4 4 6 Q6 7 5 10 M8 2 Q7 4 9 5 Q10 7 8 9" fill="none" stroke="var(--blue)" stroke-width="1.2"/></svg>
      <div class="item online">hello@mastersnow.com<br>www.mastersnow.com</div>
    </div>
  </footer>
</div>
</body>
</html>
```